Norvel Hand Wash

Design hand washes. Total 12 variants to be designed.

Variants name are:

1) MILK &OLIVE
2) Shea Butter
3) Hidden Dawn
4) Cream and Peach
5) Milk and Honey
6) Amber Whisper
7) Bakhour
8) Musk
9) White Oud
10) Black Oud
11) Rose Oud
12) Oud & Sandalwood

Labels can be on transparent sticker or background colors. All variants will be differentiated by fragrances and color. Bottle will be transparent. Pumps used for dispensing will be in Black or Transparent Color.

Designers can initially present designs of 4-5 variants initially. Later based on feedback, they can work out on more.

Bottle is 400ml and shape is rectangle. Ignore the size on bottle picture. Bottle keyline is attached.

Target Market(s)

B+, B, C+

Requirements
Must have
• Some relation to the variant names

```html
<!DOCTYPE html>
<html lang="en">
<head>
<meta charset="utf-8">
<title>Norvel Hand Wash Labels</title>
<link href="https://fonts.googleapis.com/css2?family=Playball&family=Lora:wght@500&family=Arimo:wght@700&display=swap" rel="stylesheet">
<style>
  :root {
    --olive-light: #d9fbd9;
    --olive-mid: #9ef59a;
    --olive-title: #19e81a;
    --olive-fruit: #6f7d1a;
    --olive-deep: #4b5a10;
    --rose-light: #fde3fb;
    --rose-mid: #f78ef0;
    --rose-title: #f21ee0;
    --rose-accent: #ee1111;
    --rose-petal: #f59ac8;
    --leaf: #8ce664;
    --brand-blue: #4b4fd8;
    --ink: #111111;
    --white: #ffffff;
  }
  html, body { margin: 0; padding: 0; overflow: hidden; }
  body { width: 1200px; height: 924px; background: var(--white); position: relative; }

  .label {
    position: absolute; width: 496px; height: 881px;
    border-radius: 50px; overflow: hidden;
  }
  .label--olive { left: 50px; top: 27px;
    background: radial-gradient(circle at 60% 55%, var(--white) 0%, var(--olive-light) 45%, var(--olive-mid) 100%); }
  .label--rose { left: 665px; top: 29px;
    background: radial-gradient(circle at 60% 55%, var(--white) 0%, var(--rose-light) 45%, var(--rose-mid) 100%); }

  .label__art { position: absolute; inset: 0; }

  .brand-name {
    position: absolute; left: 0; width: 492px; top: 100px; text-align: center;
    font-family: "Lora", serif; font-weight: 500; font-size: 72px; color: var(--brand-blue);
    margin: 0; line-height: 1;
  }

  .product-title {
    position: absolute; margin: 0; font-family: "Playball", cursive; font-size: 122px; line-height: 1;
    transform-origin: left top; white-space: nowrap;
    text-shadow: 3px 3px 0 var(--ink), -1px -1px 0 var(--ink), 1px -1px 0 var(--ink), -1px 1px 0 var(--ink);
  }
  .label--olive .product-title { color: var(--olive-title); }
  .label--rose .product-title { color: var(--rose-title); }
  .product-title--hand { left: 104px; top: 314px; transform: scaleX(1.28); }
  .product-title--wash { left: 106px; top: 424px; transform: scaleX(1.08); }

  .variant-name {
    position: absolute; margin: 0; font-family: "Playball", cursive; font-size: 52px; line-height: 1;
    white-space: nowrap; transform-origin: left top; transform: scaleX(1.15);
  }
  .variant-name--olive { left: 200px; top: 566px; color: var(--white);
    text-shadow: 1px 1px 0 #555, -1px -1px 0 #888; }
  .variant-name--olive .variant-name__accent { color: #9a9a12; }
  .variant-name--rose { left: 260px; top: 598px; color: var(--rose-accent);
    text-shadow: 2px 2px 0 var(--ink); }

  .illustration { position: absolute; }
  .illustration--olives { left: 50px; top: 627px; width: 242px; height: 204px;
    background: radial-gradient(closest-side, var(--olive-fruit) 0%, var(--olive-deep) 45%, rgba(75,90,16,0.5) 75%, rgba(75,90,16,0) 100%); }
  .illustration--roses { left: 18px; top: 627px; width: 188px; height: 200px;
    background: radial-gradient(closest-side, var(--rose-petal) 0%, #f7b7d8 50%, rgba(140,230,100,0.55) 80%, rgba(140,230,100,0) 100%); }

  .volume {
    position: absolute; left: 0; width: 488px; text-align: center; margin: 0;
    font-family: "Arimo", sans-serif; font-weight: 700; font-size: 32px; line-height: 1;
  }
  .volume--olive { top: 821px; color: var(--ink); }
  .volume--rose { top: 823px; color: var(--white);
    text-shadow: 1px 1px 0 #777, -1px -1px 0 #777, 1px -1px 0 #777, -1px 1px 0 #777; }
</style>
</head>
<body>

<section class="label label--olive">
  <svg class="label__art" viewBox="0 0 496 881" width="496" height="881">
    <defs>
      <linearGradient id="olive-ribbon" x1="0" y1="0" x2="1" y2="1">
        <stop offset="0" stop-color="#2ee82a"/>
        <stop offset="0.5" stop-color="#8ff58c"/>
        <stop offset="1" stop-color="#c9f8c7"/>
      </linearGradient>
      <radialGradient id="olive-oval" cx="0.5" cy="0.45" r="0.6">
        <stop offset="0" stop-color="#d6efdd"/>
        <stop offset="1" stop-color="#8fc8a0"/>
      </radialGradient>
    </defs>
    <path class="ribbon" fill="url(#olive-ribbon)" opacity="0.85"
      d="M140 0 C60 120 20 260 60 360 C100 460 240 520 300 640 C340 720 350 800 330 881 L420 881 C440 780 400 670 330 580 C250 480 100 420 110 320 C120 220 200 100 230 0 Z"/>
    <path fill="#ffffff" opacity="0.7"
      d="M410 560 C450 540 480 520 496 505 L496 600 C470 640 440 680 400 700 C380 660 390 600 410 560 Z"/>
    <ellipse cx="246" cy="157" rx="222" ry="127" fill="none" stroke="#ffffff" stroke-width="1.5"/>
    <ellipse cx="246" cy="157" rx="206" ry="111" fill="url(#olive-oval)" stroke="#ffffff" stroke-width="8"/>
  </svg>
  <h1 class="brand-name">Norvel</h1>
  <p class="product-title product-title--hand">Hand</p>
  <p class="product-title product-title--wash">Wash</p>
  <p class="variant-name variant-name--olive">Milk <span class="variant-name__accent">Olive</span></p>
  <div class="illustration illustration--olives" role="img" aria-label="Illustration of two green olives on a branch with leaves over a milk splash"></div>
  <p class="volume volume--olive">400 ml</p>
</section>

<section class="label label--rose">
  <svg class="label__art" viewBox="0 0 496 881" width="496" height="881">
    <defs>
      <linearGradient id="rose-ribbon" x1="0" y1="0" x2="1" y2="1">
        <stop offset="0" stop-color="#f01ee6"/>
        <stop offset="0.5" stop-color="#f78ef0"/>
        <stop offset="1" stop-color="#f9c6f5"/>
      </linearGradient>
      <radialGradient id="rose-oval" cx="0.5" cy="0.45" r="0.6">
        <stop offset="0" stop-color="#fcd8f8"/>
        <stop offset="1" stop-color="#f6a6ee"/>
      </radialGradient>
    </defs>
    <path class="ribbon" fill="url(#rose-ribbon)" opacity="0.85"
      d="M140 0 C60 120 20 260 60 360 C100 460 240 520 300 640 C340 720 350 800 330 881 L420 881 C440 780 400 670 330 580 C250 480 100 420 110 320 C120 220 200 100 230 0 Z"/>
    <ellipse cx="246" cy="157" rx="222" ry="127" fill="none" stroke="#ffffff" stroke-width="1.5"/>
    <ellipse cx="246" cy="157" rx="206" ry="111" fill="url(#rose-oval)" stroke="#ffffff" stroke-width="8"/>
  </svg>
  <h1 class="brand-name">Norvel</h1>
  <p class="product-title product-title--hand">Hand</p>
  <p class="product-title product-title--wash">Wash</p>
  <p class="variant-name variant-name--rose">Rose Oud</p>
  <div class="illustration illustration--roses" role="img" aria-label="Illustration of three pink roses with green leaves"></div>
  <p class="volume volume--rose">400 ml</p>
</section>

</body>
</html>
```